New Tech Support Service needs a website design

We need a web design for a new product we are developing that provides tech support to consumers for a small ongoing monthly fee. We are looking for a fresh, technology look and feel. We want the site to have a tech feel - yet not intimidating. Simple and welcoming. We are in need of an initial landing page, sign on page, and a product home page.

Thank you to everyone who submitted designs. It was a very difficult decision!

Tech

```html
<!DOCTYPE html>
<html lang="en">
<head>
<meta charset="utf-8">
<title>Tech Support Service – Landing Page</title>
<link href="https://fonts.googleapis.com/css2?family=Lato:wght@300;400;700&family=Open+Sans:wght@400&display=swap" rel="stylesheet">
<style>
  :root {
    --blue: #1a6fd8;
    --blue-dark: #0a55c4;
    --ink: #2a2a2a;
    --text: #555;
    --muted: #777;
    --rule: #dcdcdc;
    --band: #efefef;
    --footer: #2b2b2b;
    --white: #fff;
  }
  * { box-sizing: border-box; margin: 0; padding: 0; }
  html, body { width: 680px; height: 1200px; overflow: hidden; background: var(--white); }
  body { font-family: "Lato", sans-serif; color: var(--ink); }
  .page { position: relative; width: 680px; height: 1200px; overflow: hidden; }

  .site-header { position: absolute; top: 0; left: 0; width: 680px; height: 84px; }
  .brand { position: absolute; left: 47px; top: 28px; font-size: 35px; font-weight: 400; color: var(--blue); letter-spacing: -0.5px; }
  .main-nav { position: absolute; right: 48px; top: 51px; display: flex; gap: 28px; font-size: 11px; color: var(--ink); }

  .hero { position: absolute; top: 84px; left: 0; width: 680px; height: 273px;
    background: radial-gradient(ellipse at 55% 70%, #6b7684 0%, #3a4b64 45%, #1f2f4c 100%); }
  .hero-arrow { position: absolute; top: 118px; }
  .hero-arrow.prev { left: 49px; }
  .hero-arrow.next { right: 49px; }

  .features { position: absolute; top: 398px; left: 0; width: 680px; display: flex; }
  .feature { position: absolute; width: 190px; text-align: center; }
  .feature-icon { display: block; margin: 0 auto; }
  .feature-title { margin-top: 6px; font-size: 16px; font-weight: 400; color: var(--blue); }
  .feature-text { margin-top: 6px; font-size: 8.5px; line-height: 14.5px; color: var(--text); font-family: "Open Sans", sans-serif; }

  .divider { position: absolute; top: 595px; left: 50px; width: 582px; height: 1px; background: var(--rule); }

  .product-shot { position: absolute; top: 645px; left: 98px; width: 237px; height: 182px;
    background: linear-gradient(180deg, #f4f4f4 0%, #e4e4e4 20%, #8c8f86 30%, #6e6d66 45%, #f6f6f6 55%, #fafafa 100%);
    box-shadow: 0 1px 4px rgba(0,0,0,0.2); }
  .product-zoom { position: absolute; top: 635px; left: 51px; width: 116px; height: 116px; border-radius: 50%;
    border: 5px solid var(--white); box-shadow: 0 1px 5px rgba(0,0,0,0.25);
    background: linear-gradient(180deg, #f3f5ee 0%, #f3f5ee 42%, #9aa08f 43%, #6f7566 100%); }
  .about { position: absolute; top: 655px; left: 363px; width: 270px; }
  .about-title { font-size: 18.5px; font-weight: 400; color: var(--ink); }
  .about-text { margin-top: 8px; font-size: 8.2px; line-height: 14px; color: var(--text); font-family: "Open Sans", sans-serif; }
  .btn-start { display: inline-flex; align-items: center; gap: 8px; margin-top: 12px; height: 20px; padding: 0 10px;
    border: 1px solid var(--blue); border-radius: 11px; font-size: 9.5px; color: var(--blue); }

  .testimonials { position: absolute; top: 878px; left: 0; width: 680px; height: 253px; background: var(--band); text-align: center; }
  .testimonials-title { margin-top: 26px; font-size: 18.5px; font-weight: 400; color: var(--ink); }
  .avatar { display: block; width: 82px; height: 82px; margin: 9px auto 0; border-radius: 50%; border: 2px solid var(--white);
    background: radial-gradient(circle at 50% 40%, #e8d2c0 0%, #c7a78b 60%, #f2f2f2 100%); box-shadow: 0 0 3px rgba(0,0,0,0.2); }
  .quote { margin-top: 19px; font-family: "Open Sans", sans-serif; font-size: 9.7px; line-height: 18px; color: var(--ink); }
  .quote-author { position: absolute; right: 77px; top: 196px; font-family: "Open Sans", sans-serif; font-size: 9.5px; color: var(--ink); }
  .quote-author small { font-size: 8px; color: var(--muted); }
  .dots { position: absolute; top: 225px; left: 320px; display: flex; gap: 2px; }
  .dot { width: 8px; height: 8px; border-radius: 50%; background: #d4d4d4; border: 1px solid #aaa; }
  .dot.active { background: #666; }

  .site-footer { position: absolute; top: 1131px; left: 0; width: 680px; height: 69px; background: var(--footer); color: var(--white);
    font-family: "Open Sans", sans-serif; font-size: 8.3px; }
  .footer-links { position: absolute; left: 61px; top: 18px; }
  .copyright { position: absolute; left: 61px; top: 39px; }
  .social { position: absolute; left: 512px; top: 15px; display: flex; gap: 8px; }
  .social-item { width: 20px; height: 20px; background: var(--blue); }
</style>
</head>
<body>
<div class="page">

  <header class="site-header">
    <div class="brand">Logo</div>
    <nav class="main-nav">
      <span>Home</span><span>About Us</span><span>Services</span><span>Testimonials</span><span>Contact</span>
    </nav>
  </header>

  <section class="hero" role="img" aria-label="Hand holding a smartphone with floating translucent app tiles">
    <svg class="hero-arrow prev" width="32" height="30" viewBox="0 0 32 30"><path d="M30 15H3M15 2L2 15l13 13" fill="none" stroke="#fff" stroke-width="1.6"/></svg>
    <svg class="hero-arrow next" width="32" height="30" viewBox="0 0 32 30"><path d="M2 15h27M17 2l13 13-13 13" fill="none" stroke="#fff" stroke-width="1.6"/></svg>
  </section>

  <section class="features">
    <div class="feature" style="left:51px">
      <svg class="feature-icon" width="74" height="80" viewBox="0 0 74 80">
        <polygon points="37,2 71,20 71,60 37,78 3,60 3,20" fill="var(--blue-dark)" stroke-linejoin="round"/>
        <path d="M19 40l34-14-8 30-10-8-4 8v-10l14-12-17 11z" fill="#fff"/>
      </svg>
      <h3 class="feature-title">Services</h3>
      <p class="feature-text">Claritas est eteus dynamicuin thts,<br>qui sequitur mutatiem consuetud Claritas<br>dynamicusClaritas est etiam procss</p>
    </div>
    <div class="feature" style="left:245px">
      <svg class="feature-icon" width="74" height="80" viewBox="0 0 74 80">
        <polygon points="37,2 71,20 71,60 37,78 3,60 3,20" fill="var(--blue-dark)"/>
        <circle cx="37" cy="40" r="15" fill="none" stroke="#fff" stroke-width="5" stroke-dasharray="4 3.8"/>
        <circle cx="37" cy="40" r="11" fill="#fff"/>
        <path d="M30 36c3-2 5 0 7 2s1 5-2 6M40 33c2 2 4 3 6 3M38 49c1-3 4-4 6-3" fill="none" stroke="var(--blue-dark)" stroke-width="2"/>
      </svg>
      <h3 class="feature-title">Technologies</h3>
      <p class="feature-text">Claritas est eteus dynamicuin thts,<br>qui sequitur mutatiem consuetud Claritas<br>dynamicusClaritas est etiam procss</p>
    </div>
    <div class="feature" style="left:436px">
      <svg class="feature-icon" width="74" height="80" viewBox="0 0 74 80">
        <polygon points="37,2 71,20 71,60 37,78 3,60 3,20" fill="var(--blue-dark)"/>
        <path d="M37 22a13 13 0 0 0-8 23v5h16v-5a13 13 0 0 0-8-23z" fill="none" stroke="#fff" stroke-width="3"/>
        <rect x="34.5" y="28" width="5" height="10" rx="1" fill="#fff"/>
        <circle cx="37" cy="42" r="2.5" fill="#fff"/>
        <path d="M30 54h14M31 58h12" stroke="#fff" stroke-width="2.6"/>
      </svg>
      <h3 class="feature-title">Consulting</h3>
      <p class="feature-text">Claritas est eteus dynamicuin thts,<br>qui sequitur mutatiem consuetud Claritas<br>dynamicusClaritas est etiam procss</p>
    </div>
  </section>

  <div class="divider"></div>

  <div class="product-shot" role="img" aria-label="Screenshot of the product website on a browser page"></div>
  <div class="product-zoom" role="img" aria-label="Magnified detail of the product website header"></div>

  <section class="about">
    <h2 class="about-title">About Our Product</h2>
    <p class="about-text">Claritas est etiam processus dynamicus, qui sequitur mutationem consuetud ium lectorum. Mirum est notare quam littera gothica, quam nunc putamus pa rum claram, anteposuerit litterarum formas humanitatis per.<br>Duis autem vel eum iriure dolor in hendrerit in vulputate velit esse molestie c onsequat, vel illum dolore eu feugiat nulla facilisis at vero eros et accumsane t iusto odio dignissim qui blandit praesent luptatum zzril delenit.</p>
    <span class="btn-start">Get Started
      <svg width="12" height="10" viewBox="0 0 12 10"><path d="M1 5h9M6 1l4 4-4 4" fill="none" stroke="var(--blue)" stroke-width="1.5"/></svg>
    </span>
  </section>

  <section class="testimonials" role="group" aria-label="Client testimonials over a faint grid of portrait photos">
    <h2 class="testimonials-title">Client Testimonials</h2>
    <div class="avatar" role="img" aria-label="Client portrait photo"></div>
    <p class="quote">I am so happy to have met you! Before Clearpath Coaching, I had vocal<br>problems that clouded my mind and made it zero fun to sing. Now I sing again and even have a weekly job as a speaker.</p>
    <p class="quote-author">- Marek, <small>Germany</small></p>
    <div class="dots"><span class="dot active"></span><span class="dot"></span><span class="dot"></span><span class="dot"></span></div>
  </section>

  <footer class="site-footer">
    <p class="footer-links">Terms and Conditions | Privacy Promise | FAQ's | Contact Us</p>
    <p class="copyright">Copyright © 2013. All Rights Reserved.</p>
    <div class="social">
      <span class="social-item" aria-label="Social link"></span>
      <span class="social-item" aria-label="Social link"></span>
      <span class="social-item" aria-label="Feed link"></span>
      <span class="social-item" aria-label="Video link"></span>
    </div>
  </footer>

</div>
</body>
</html>
```